Constructor Company /Carpenter

We need a high quality design for a Brochure up to 8pages.Copmany does plastering, building houses, make renovation of houses.
Updates

Ich brauche zusätzliche Tage um durchzusehen

Target Market(s)

The Brochure is a high quality hand out for architects.

Industry/Entity Type

Construction Company

Font styles to use
Sans Serif

Colors

Designer to choose colors to be used in the design.

Requirements
Must have
• You can build the brochure like the website www.novaris-bau.ch is built. The brochure needs to look clean, modern and professionell.
• The brochure need to have the same colors like website www.novaris-bau.ch

```html
<!DOCTYPE html>
<html lang="en">
<head>
<meta charset="utf-8">
<title>Novaris Bau GmbH – Company Profile Brochure</title>
<link href="https://fonts.googleapis.com/css2?family=Montserrat:wght@400;500;600;700&family=Roboto+Condensed:wght@400;700&display=swap" rel="stylesheet">
<style>
:root{
  --blue:#0a47a0;
  --blue-dark:#063a86;
  --ink:#111;
  --grey:#5c5c5c;
  --light:#efefef;
  --stage:#c9c9c9;
  --white:#fff;
}
*{margin:0;padding:0;box-sizing:border-box}
html,body{width:1200px;height:2382px;overflow:hidden}
body{background:var(--stage);font-family:"Montserrat",sans-serif;color:var(--ink);position:relative}
.label{position:absolute;font:500 23px "Montserrat",sans-serif;letter-spacing:.5px;color:#222;text-align:center;width:490px}
.page{position:absolute;width:490px;height:692px;background:var(--white);overflow:hidden;box-shadow:0 2px 6px rgba(0,0,0,.25)}
.abs{position:absolute}
.photo{position:absolute}
.brand{display:flex;align-items:center;gap:8px;font-family:"Montserrat",sans-serif;font-weight:500;color:var(--ink);white-space:nowrap}
.brand .mark{background:var(--blue);display:block;flex:none}
.footer-note{font-size:8px;font-weight:600}
/* cover 1 */
.c1-title{left:46px;top:318px;width:394px;height:160px;background:var(--blue);display:flex;align-items:center;justify-content:center;text-align:center}
.c1-title::after{content:"";position:absolute;inset:9px;border:1.5px solid rgba(255,255,255,.8)}
.c1-title h1{font:700 32px/1.2 "Roboto Condensed",sans-serif;color:#fff;letter-spacing:.3px}
.c1-meta{left:0;width:490px;top:490px;text-align:center;font:400 15px "Roboto Condensed",sans-serif;color:var(--blue)}
.c1-brand{left:0;width:490px;top:530px;justify-content:center;font-size:32px}
.c1-footer{left:0;bottom:0;width:490px;height:58px;background:linear-gradient(#2a2a2a,#0d0d0d);color:#fff;display:flex;justify-content:space-between;align-items:center;padding:0 24px}
.c1-footer .url{font-size:12px;font-weight:600}
/* cover 2 */
.c2-address{right:36px;top:56px;text-align:right;font:400 11px/1.35 "Montserrat",sans-serif;color:#333}
.c2-address b{font-weight:700}
.c2-band{left:0;top:202px;width:465px;height:155px;background:var(--blue);padding:20px 42px}
.c2-band h1{font:700 26px/1.22 "Montserrat",sans-serif;color:#fff}
.c2-band p{font:400 11px "Montserrat",sans-serif;color:#fff;margin-top:10px}
.c2-strip{left:425px;top:202px;width:40px;height:155px;background:var(--blue-dark)}
.c2-grey{left:425px;top:128px;width:40px;height:74px;background:#999}
.c2-footer{left:22px;right:24px;bottom:8px;display:flex;justify-content:space-between;align-items:center;font:400 9px "Montserrat",sans-serif;color:#555}
.c2-footer .url{font:700 15px "Montserrat",sans-serif;color:var(--blue)}
/* inner 1 */
.services-frame{left:20px;top:325px;width:440px;height:145px;border:1px solid #777}
.services-frame .brand{position:absolute;top:-18px;left:50%;transform:translateX(-50%);background:#fff;padding:0 10px;font-size:24px}
.service{position:absolute;top:40px;width:70px;text-align:center;font-size:9px;font-weight:600}
.service .icon{width:60px;height:60px;margin:0 auto 6px;background:linear-gradient(135deg,#e9e9e9,#c5d3ea);border:1.5px solid #222}
.tp h2{font:700 11px "Montserrat",sans-serif;color:var(--blue);margin-bottom:8px}
.tp p{font-size:7px;line-height:1.35;color:#333;margin-bottom:8px}
.expect{left:290px;top:492px;width:176px;height:150px;background:var(--blue);color:#fff;padding:14px 16px}
.expect h2{font:700 13px/1.2 "Montserrat",sans-serif;text-align:center;margin-bottom:10px}
.expect li{list-style:none;font-size:7.5px;font-weight:600;margin-bottom:4px;display:flex;align-items:center;gap:5px}
.pgnum{width:12px;height:12px;border-radius:50%;background:var(--blue);color:#fff;font-size:7px;display:flex;align-items:center;justify-content:center}
/* inner 2 */
.sec-title{left:36px;width:418px;height:40px;border:1px solid var(--blue);display:flex;align-items:center;justify-content:center;font:600 14px "Montserrat",sans-serif}
.sec-lead{left:38px;width:410px;font-size:7px;line-height:1.35}
.sec-list{left:38px;width:130px;font-size:7px;line-height:1.35}
.sec-list b{display:block;margin:6px 0 4px;font-size:7px}
.benefits{display:flex;flex-direction:column;justify-content:center;gap:10px;padding-left:20px}
.benefit{width:120px;text-align:center;color:#fff;font-size:7.5px;font-weight:600}
.benefit svg{display:block;margin:0 auto 3px}
.blue-half{left:0;top:345px;width:490px;height:347px;background:var(--blue);color:#fff}
</style>
</head>
<body>

<div class="label" style="left:108px;top:829px">COVER PAGE 1</div>
<div class="label" style="left:615px;top:829px">COVER PAGE 2</div>
<div class="label" style="left:108px;top:2309px">INNER PAGE 1</div>
<div class="label" style="left:615px;top:2309px">INNER PAGE 2</div>

<!-- Cover page 1 -->
<section class="page cover-one" style="left:108px;top:870px;border-top:4px solid var(--blue)">
  <div class="photo" role="img" aria-label="Photo of a hand plastering a wall with a trowel" style="left:0;top:0;width:490px;height:380px;background:linear-gradient(100deg,#6b6e70 0%,#b08a72 35%,#9c9d9b 55%,#c9c7c1 100%)"></div>
  <div class="abs" style="left:0;top:380px;width:490px;height:250px;background:linear-gradient(#e6e6e6,#fdfdfd)"></div>
  <div class="abs" style="left:34px;top:306px;width:422px;height:172px;background:#e8e8e8"></div>
  <div class="abs c1-title"><h1>YOUR PLASTERER FROM<br>AESCH IN BASEL AND<br>SURROUNDINGS</h1></div>
  <div class="abs c1-meta">Company Profile &nbsp;|&nbsp; Oct 2019</div>
  <div class="abs brand c1-brand"><span class="mark" style="width:30px;height:30px"></span>Novaris Bau GmbH</div>
  <div class="abs c1-footer"><span class="footer-note">Do You Have Questions? Give us a call! 079 000 12 34</span><span class="url">www.novaris-bau.ch</span></div>
</section>

<!-- Cover page 2 -->
<section class="page cover-two" style="left:615px;top:870px">
  <div class="abs brand" style="left:40px;top:58px;font-size:22px"><span class="mark" style="width:22px;height:22px"></span>Novaris Bau GmbH</div>
  <div class="abs c2-address"><b>Address of Company:</b><br>LINDENWEG<br>8, 4147 AESCH</div>
  <div class="abs c2-grey"></div>
  <div class="abs c2-band"><h1>YOUR PLASTERER FROM<br>AESCH IN BASEL AND<br>SURROUNDINGS</h1><p>Company Profile &nbsp;|&nbsp; Oct 2019</p></div>
  <div class="abs c2-strip"></div>
  <div class="photo" role="img" aria-label="Photo of a hand plastering a wall with a trowel" style="left:0;top:357px;width:465px;height:300px;background:linear-gradient(100deg,#8a7c70 0%,#b9906f 40%,#9fa09d 60%,#c6c4be 100%)"></div>
  <div class="abs c2-footer"><span>Do You Have Questions? Give us a call! 079 000 12 34</span><span class="url">www.novaris-bau.ch</span></div>
</section>

<!-- Inner page 1 -->
<section class="page inner-one" style="left:108px;top:1583px">
  <div class="photo" role="img" aria-label="Photo of a room under renovation with brick wall, ladder and wooden floor" style="left:0;top:0;width:490px;height:277px;background:linear-gradient(90deg,#9a7a66 0%,#b9b6b0 40%,#d9d7d3 75%,#c9c4bc 100%)"></div>
  <div class="abs services-frame">
    <div class="brand"><span class="mark" style="width:22px;height:22px"></span>Novaris Bau GmbH</div>
    <div class="service" style="left:10px"><div class="icon" role="img" aria-label="Facade icon"></div>facades</div>
    <div class="service" style="left:98px"><div class="icon" role="img" aria-label="Plaster trowel icon"></div>plaster</div>
    <div class="service" style="left:186px"><div class="icon" role="img" aria-label="Paint roller icon"></div>To paint</div>
    <div class="service" style="left:274px"><div class="icon" role="img" aria-label="Floor plan icon"></div>modification</div>
    <div class="service" style="left:362px"><div class="icon" role="img" aria-label="Garden tools icon"></div>gardening</div>
  </div>
  <div class="abs tp" style="left:32px;top:513px;width:220px">
    <h2>TRADITION AND PASSION</h2>
    <p>Our clients benefit from the experience we have gained over the past decades in our craft. We specialize in plasterer, facade and painting work.</p>
    <p>Our way of working allows a perfect on-time execution to the best quality.</p>
    <p>We are happy to hand you over our personal references on request.</p>
  </div>
  <div class="abs expect">
    <h2>WHAT YOU CAN<br>EXPECT FROM US:</h2>
    <ul>
      <li>⌂ Qualitatively perfect work</li>
      <li>⌂ Adhering to the schedules</li>
      <li>⌂ Individual advice</li>
      <li>⌂ Detailed cost statement</li>
      <li>⌂ Fair price-performance ratio</li>
    </ul>
  </div>
  <div class="abs" style="left:32px;top:658px;width:428px;border-top:1px solid #bbb"></div>
  <div class="abs footer-note" style="left:32px;top:670px;font-size:7px">Do You Have Questions? Give us a call! 079 000 12 34</div>
  <div class="abs pgnum" style="left:448px;top:652px">1</div>
</section>

<!-- Inner page 2 -->
<section class="page inner-two" style="left:615px;top:1583px">
  <div class="abs brand" style="left:40px;top:18px;font-size:15px"><span class="mark" style="width:16px;height:16px"></span>Novaris Bau GmbH</div>
  <div class="abs" style="right:38px;top:30px;font-size:7px;font-weight:600">www.novaris-bau.ch</div>
  <div class="abs sec-title" style="top:68px;color:var(--blue)">FACADES IN BASEL, BASEL-LAND AND AARGAU</div>
  <div class="abs sec-lead" style="top:130px">We are your specialists for your wishes in the field of plasters and renovations. Our many years of professional experience makes us a specialist for your plaster work indoors and outdoors.</div>
  <div class="abs sec-list" style="top:158px"><b>We offer the following services:</b>Fassadenputze<br>basement insulation<br>ceiling insulation<br>Perimeter insulation<b>YOU BENEFIT FROM:</b>heat protection<br>Energy saving<br>soundproofing<br>Fire protection<br>nice aesthetics</div>
  <div class="abs benefits" role="img" aria-label="Brick wall photo fading into blue with benefit icons" style="left:180px;top:162px;width:270px;height:160px;background:linear-gradient(90deg,var(--blue) 0%,var(--blue) 35%,#7d9bc7 65%,#b0623e 100%)">
    <div class="benefit"><svg width="18" height="18" viewBox="0 0 18 18"><circle cx="9" cy="9" r="8" fill="#fff"/><text x="9" y="13" text-anchor="middle" font-size="11" font-weight="700" fill="#0a47a0">$</text></svg>MAKING COST-EFFECTIVE</div>
    <div class="benefit"><svg width="16" height="16" viewBox="0 0 16 16"><path d="M2 7h3v8H2zM6 7l3-6c2 0 2 2 1 5h4l-1 9H6z" fill="#fff"/></svg>QUALITATIVELY</div>
    <div class="benefit"><svg width="18" height="16" viewBox="0 0 18 16"><path d="M2 15V9h3v6zM7 15V6h3v9zM12 15V3h3v12z M1 8l6-5 3 3 6-5" fill="#fff" stroke="#fff"/></svg>EFFICIENT</div>
  </div>
  <div class="abs blue-half">
    <div class="abs sec-title" style="top:24px;border-color:#fff;color:#fff">PLASTERING IN BASEL, BASEL-LAND AND AARGAU</div>
    <div class="abs sec-lead" style="top:88px">We are your specialists for your wishes in the field of plasters and renovations. Our many years of professional experience makes us a specialist for your plaster work indoors and outdoors.</div>
    <div class="abs sec-list" style="top:112px"><b>We offer the following services:</b>Gipserarbeiten<br>Renovations<br>insulations<br>Clay plasters<br>isolations<br>Altbausanierungen<br>Renovating facades<br>Various mineral abrasions<br>basic plasters<br>fillings<br>Special plasters<br>drywall<br>Kittfugen</div>
    <div class="abs benefits" role="img" aria-label="Photo of a plaster bucket with trowel on a dark background with benefit icons" style="left:180px;top:122px;width:270px;height:160px;background:linear-gradient(90deg,#0b0b0b 0%,#1a1a1a 45%,#8d8a84 80%,#c9c5bd 100%)">
      <div class="benefit"><svg width="18" height="18" viewBox="0 0 18 18"><circle cx="9" cy="9" r="8" fill="#fff"/><text x="9" y="13" text-anchor="middle" font-size="11" font-weight="700" fill="#111">$</text></svg>MAKING COST-EFFECTIVE</div>
      <div class="benefit"><svg width="16" height="16" viewBox="0 0 16 16"><path d="M2 7h3v8H2zM6 7l3-6c2 0 2 2 1 5h4l-1 9H6z" fill="#fff"/></svg>QUALITATIVELY</div>
      <div class="benefit"><svg width="18" height="16" viewBox="0 0 18 16"><path d="M2 15V9h3v6zM7 15V6h3v9zM12 15V3h3v12z M1 8l6-5 3 3 6-5" fill="#fff" stroke="#fff"/></svg>EFFICIENT</div>
    </div>
    <div class="abs footer-note" style="left:32px;top:322px;font-size:7px">Do You Have Questions? Give us a call! 079 000 12 34</div>
    <div class="abs pgnum" style="left:440px;top:318px;background:#fff;color:var(--blue)">2</div>
  </div>
</section>
</body>
</html>
```